Business cards for start-up accounting firm

I'm looking for a double sided business card ready for upload into Lumo print or similar print providers with no modification required by me.
I'm looking for something simple as i think cards that are too 'busy' actually detract from the message. I have some thoughts but more than happy to see what comes up. The logo i have came out of left field and i love it the moment i saw it!

My thoughts:

Side 1: Just the logo, perhaps on a dark grey or charcoal background to make the logo colours stand out?

Side 2: The call to action from me website 'Looking for a more relaxed, friendly and interactive relationship with your accountant?' with my contact information
Name: Gus Tarrow
Email: gus@ledgerowl.com.au
Website: www.ledgerowl.com.au
Phone: 1300 762 349

The call to action needs to be the first thing they see when they look at side 2. If it helps to know what we do and how we do it there is a draft website at www.ledgerowl.com.au

Like i said, happy to consider anything that comes up :)

Target Market(s)

i'm targeting small business owners who experience a lot of stress around finacial reporting and have had bad experiences with accountants in the past.

Industry/Entity Type

Accounting

Contact Information for Business Card

Contained in the Description

Font styles to use
Serif
Sans Serif
Other font styles liked:
• See logo files attached

Colors
474747

Requirements
Must have
• My logo, slogan and contact information

```html
<!DOCTYPE html>
<html lang="en">
<head>
<meta charset="utf-8">
<title>Ledger Owl – Business Cards</title>
<link rel="stylesheet" href="https://fonts.googleapis.com/css2?family=Source+Sans+3:wght@400;600;700&display=swap">
<style>
  :root {
    --stage: #474747;
    --card: #141414;
    --purple: #9a3fae;
    --yellow: #f2c40f;
    --white: #f2f2f2;
    --divider: #5a5a5a;
  }
  * { box-sizing: border-box; margin: 0; padding: 0; }
  html, body { width: 1200px; height: 814px; overflow: hidden; }
  body {
    background: var(--stage);
    font-family: "Source Sans 3", sans-serif;
    position: relative;
  }
  .card {
    position: absolute;
    top: 252px;
    width: 540px;
    height: 310px;
    background: var(--card);
    border-radius: 4px;
    box-shadow: 0 6px 18px rgba(0,0,0,.35);
  }
  .card--front { left: 40px; }
  .card--back { left: 620px; }

  /* front */
  .brand {
    position: absolute;
    left: 36px;
    top: 132px;
    width: 232px;
    text-align: center;
  }
  .brand__name {
    font-weight: 700;
    font-size: 42px;
    line-height: 1;
    color: var(--yellow);
    letter-spacing: .5px;
  }
  .divider {
    position: absolute;
    left: 290px;
    top: 78px;
    width: 1px;
    height: 150px;
    background: var(--divider);
  }
  .contact {
    position: absolute;
    left: 312px;
    top: 92px;
  }
  .contact__name {
    font-weight: 600;
    font-size: 22px;
    color: var(--purple);
    margin-bottom: 12px;
  }
  .contact__list { list-style: none; }
  .contact__item {
    display: flex;
    align-items: center;
    gap: 9px;
    font-size: 15px;
    color: var(--white);
    line-height: 24px;
  }
  .contact__icon { width: 14px; height: 14px; flex: none; }

  /* back */
  .back__name {
    position: absolute;
    left: 0; right: 0;
    top: 86px;
    text-align: center;
    font-weight: 700;
    font-size: 46px;
    color: var(--purple);
  }
  .back__cta {
    position: absolute;
    left: 0; right: 0;
    top: 200px;
    text-align: center;
    font-size: 15px;
    line-height: 20px;
    color: var(--white);
  }
</style>
</head>
<body>

<section class="card card--front" aria-label="Card front">
  <div class="brand">
    <div class="brand__name">Ledger Owl</div>
  </div>

  <div class="divider"></div>

  <div class="contact">
    <p class="contact__name">Gus Tarrow</p>
    <ul class="contact__list">
      <li class="contact__item">
        <svg class="contact__icon" viewBox="0 0 14 14" aria-hidden="true">
          <path fill="var(--purple)" d="M3 1.2l2 .2 1 3-1.4 1.1a7 7 0 0 0 3.9 3.9L9.6 8l3 1 .2 2-1.6 1.6C6 12.6 1.4 8 1.4 2.8z"/>
        </svg>
        1300 762 349
      </li>
      <li class="contact__item">
        <svg class="contact__icon" viewBox="0 0 14 14" aria-hidden="true">
          <rect x="1" y="3" width="12" height="8.5" rx="1" fill="var(--purple)"/>
          <path d="M1.5 3.6L7 8l5.5-4.4" fill="none" stroke="var(--card)" stroke-width="1.2"/>
        </svg>
        gus@ledgerowl.com.au
      </li>
      <li class="contact__item">
        <svg class="contact__icon" viewBox="0 0 14 14" aria-hidden="true">
          <circle cx="7" cy="7" r="6.2" fill="var(--purple)"/>
          <path d="M1 7h12M7 .8c-2.6 3.6-2.6 8.8 0 12.4M7 .8c2.6 3.6 2.6 8.8 0 12.4" fill="none" stroke="var(--card)" stroke-width="1"/>
        </svg>
        ledgerowl.com.au
      </li>
    </ul>
  </div>
</section>

<section class="card card--back" aria-label="Card back">
  <div class="back__name">Ledger Owl</div>
  <p class="back__cta">Looking for a more relaxed, friendly and<br>interactive relationship with your accountant?</p>
</section>

</body>
</html>
```